Online-Marketing Material für Podcast
Zielgruppe
eCommerce Podcast
Aufgabenstellung
Wir benötigen eine ansprechende und professionelle Grafik für unseren Podcast 'LAUBFROSCH FUNKSTUNDE'. Diese Grafik wird in verschiedenen digitalen Plattformen verwendet, einschließlich Podcast-Playern und sozialen Medien. Titel/Logo:
Text: 'LAUBFROSCH FUNKSTUNDE'
Farbe: Weiß
Schriftart: Dick und gut lesbar (z.B. eine Sans-Serif Schriftart wie Arial Black oder Helvetica Bold)
Platzierung: Prominent und zentral oder oberhalb der Bilder von uns beiden
Bilder:
Bilder von den Hosts: Bild von mir (Host 1) und Bild von Reinhold (Host 2) sind angehängt.
Integration: Beide Bilder sollen prominent und harmonisch in das Design integriert werden. Idealerweise werden die Bilder nebeneinander oder leicht überlappend platziert.
Stil: Bitte stellt sicher, dass die Bilder gut ausgeschnitten und bearbeitet sind, sodass sie professionell aussehen und sich gut in den Hintergrund einfügen.
Hintergrund und Farbschema:
Hintergrundfarbe: Dunkel (z.B. ein dunkles Blau oder Grau), um einen guten Kontrast zum weißen Text zu bieten.
Zusätzliche Elemente/Farben: Dezente Akzente, die zur E-Commerce-Thematik passe aber der Fokus sollte auf dem Titel und unseren Bildern liegen.
Größe und Format:
Die Grafik sollte in einem quadratischen Format erstellt werden (z.B. 3000x3000 Pixel) und in hoher Auflösung vorliegen.
Dateiformat: PNG oder JPEG, wobei PNG bevorzugt wird, da es eine höhere Qualität bietet.
Zusätzliche Hinweise:
Der Gesamteindruck der Grafik sollte modern, dynamisch und professionell sein.
Der Podcast soll als seriöse und informative Quelle im E-Commerce-Bereich wahrgenommen werden, daher sollte das Design diese Professionalität widerspiegeln.

```html
<!DOCTYPE html>
<html lang="de">
<head>
<meta charset="utf-8">
<title>Laubfrosch Funkstunde – Podcast Cover</title>
<link rel="stylesheet" href="https://fonts.googleapis.com/css2?family=Roboto:wght@900&display=swap">
<style>
  :root {
    --navy-deep: #060a22;
    --navy: #0c1438;
    --navy-band: #1a2a66;
    --navy-band-light: #2a3f8a;
    --glow: #c9ccd6;
    --title: #ffffff;
    --host-left-top: #5a463a;
    --host-left-mid: #e8c7b0;
    --host-left-bottom: #f6f6f4;
    --host-right-top: #7a5a40;
    --host-right-mid: #e9c6ae;
    --host-right-bottom: #1d1e22;
  }
  html, body {
    margin: 0;
    padding: 0;
    width: 1200px;
    height: 1200px;
    overflow: hidden;
    background: var(--navy-deep);
  }
  .cover {
    position: relative;
    width: 1200px;
    height: 1200px;
    overflow: hidden;
  }
  .cover svg {
    position: absolute;
    inset: 0;
    display: block;
  }
  .title-text {
    font-family: "Roboto", Arial, sans-serif;
    font-weight: 900;
    fill: var(--title);
  }
</style>
</head>
<body>
<main class="cover">
  <svg class="backdrop" width="1200" height="1200" viewBox="0 0 1200 1200" aria-hidden="true">
    <defs>
      <radialGradient id="stage-glow" cx="700" cy="720" r="560" gradientUnits="userSpaceOnUse">
        <stop offset="0" stop-color="var(--glow)"/>
        <stop offset="0.35" stop-color="#7c8299"/>
        <stop offset="0.75" stop-color="var(--navy)"/>
        <stop offset="1" stop-color="var(--navy-deep)"/>
      </radialGradient>
    </defs>
    <rect class="backdrop-base" width="1200" height="1200" fill="url(#stage-glow)"/>
    <!-- sweeping accent bands -->
    <g class="accent-bands" fill="none" stroke-linecap="round">
      <path d="M-60 260 C 80 80, 260 0, 520 -40" stroke="var(--navy-band)" stroke-width="70" opacity="0.55"/>
      <path d="M-80 430 C 60 200, 260 60, 560 0" stroke="var(--navy-band)" stroke-width="40" opacity="0.4"/>
      <path d="M-40 620 C 40 420, 180 240, 420 110" stroke="var(--navy-band)" stroke-width="26" opacity="0.3"/>
      <path d="M900 -40 C 1080 120, 1180 320, 1240 520" stroke="var(--navy-band)" stroke-width="60" opacity="0.35"/>
      <path d="M1000 520 C 1120 700, 1170 900, 1180 1220" stroke="var(--navy-band-light)" stroke-width="70" opacity="0.55"/>
      <path d="M1060 480 C 1180 640, 1240 820, 1250 1000" stroke="var(--navy-band-light)" stroke-width="40" opacity="0.5"/>
      <path d="M930 620 C 1040 800, 1090 1000, 1100 1220" stroke="var(--navy-band)" stroke-width="30" opacity="0.45"/>
    </g>
  </svg>

  <svg class="masthead" width="1200" height="1200" viewBox="0 0 1200 1200">
    <text class="title-text title-top" x="155" y="199" font-size="90" textLength="541" lengthAdjust="spacingAndGlyphs">LAUBFROSCH</text>
    <text class="title-text title-main" x="52" y="357" font-size="180" textLength="1100" lengthAdjust="spacingAndGlyphs">FUNKSTUNDE</text>
  </svg>

  <svg class="hosts" width="1200" height="1200" viewBox="0 0 1200 1200">
    <defs>
      <linearGradient id="host-left-tone" x1="0" y1="0" x2="0" y2="1">
        <stop offset="0" stop-color="var(--host-left-top)"/>
        <stop offset="0.12" stop-color="var(--host-left-mid)"/>
        <stop offset="0.45" stop-color="var(--host-left-mid)"/>
        <stop offset="0.6" stop-color="var(--host-left-bottom)"/>
        <stop offset="1" stop-color="var(--host-left-bottom)"/>
      </linearGradient>
      <linearGradient id="host-right-tone" x1="0" y1="0" x2="0" y2="1">
        <stop offset="0" stop-color="var(--host-right-top)"/>
        <stop offset="0.12" stop-color="var(--host-right-mid)"/>
        <stop offset="0.42" stop-color="var(--host-right-mid)"/>
        <stop offset="0.55" stop-color="var(--host-right-bottom)"/>
        <stop offset="1" stop-color="var(--host-right-bottom)"/>
      </linearGradient>
    </defs>
    <path class="host-photo host-left" role="img" aria-label="Portraitfoto Host 1 im weißen Poloshirt"
          d="M55 1200 L60 860 C70 790 150 760 230 730 L220 560 C200 420 250 310 345 308 C440 306 490 400 480 540 L470 720 C530 760 580 790 590 830 L580 1200 Z"
          fill="url(#host-left-tone)"/>
    <path class="host-photo host-right" role="img" aria-label="Portraitfoto Host 2 im schwarzen Polohemd"
          d="M515 1200 L525 860 C540 800 600 780 650 755 L590 560 C560 420 600 322 720 318 C830 315 880 410 865 560 L830 740 C960 760 1110 800 1140 880 L1160 1200 Z"
          fill="url(#host-right-tone)"/>
  </svg>
</main>
</body>
</html>
```